I need a new business card for my hair salon based in Fairfax, VA called "Lune's Salon". I have been in business at the same location for the past 15 years, and have recently remodeled the place to be a little bit more upscale and modern. Previously, my clientele's were mostly men, but now I would like to attract more female clientele into my business. I would like the design to attract the female's attention with it's modern touch, flowery, freshness with just enough information and not too compact. Simple, clean and professional is the look.
Requirements
Must Have:
- The design should include:
Business name: Lune's Salon
Hairstylist/Owner Name: Lune Okafor
Phone Number: (555) 418-6037
Website: www.lunehairstudio.example
Address: 48390 Harlow Penn Circle
Fairfax, VA 20517
FRONT CARD should include:
- Logo (Business name)
- Slogan (Soft curls, bright days)
BACK CARD should include:
- Logo (Business name)
- Hairstyle name
- Phone number
- Website
- Address
Reason: There were some good submission for this project, but most of the submission were poorly designed, and did not have what I want. There isn't enough designs for me to choose from and not one of it stood out to me. I would like to extend it a bit longer to see if any other designer would step up to the plate, and deliver. Thank you.
Requirements
Must have
- The front side of the business card should only have the business name (Lune's Salon) and slogan, (Soft curls bright days) with a creative design.
The back side of the business card should have all the business information, and creative design that matches with the front, but not identical.
The first letter (V) in (Lune's) should have a flower design connected to it, which blends into the background design.
Nice to have
- Light color scheme.
Should not have
- The front, and back should not have the same design.
Do not include illustrations of a pair of scissors, combs or any objects in the design.
The design should not take the main focus from the business name and business information. It should blend well together... if that's possible.

```html
<!DOCTYPE html>
<html lang="en">
<head>
<meta charset="utf-8">
<title>Lune's Salon — Business Card</title>
<link rel="stylesheet" href="https://fonts.googleapis.com/css2?family=Source+Sans+3:wght@400;600;700&display=swap">
<style>
  :root {
    --stage: #efe9d8;
    --card: #ffffff;
    --lavender: #9b7cf8;
    --lavender-soft: #b4a2f5;
    --violet-text: #7550e4;
    --ink: #1b1b1b;
    --slate: #8b9a9a;
    --label: #6b6656;
  }
  * { box-sizing: border-box; margin: 0; padding: 0; }
  html, body { width: 1200px; height: 982px; overflow: hidden; }
  body {
    position: relative;
    background: var(--stage);
    font-family: "Source Sans 3", "Source Sans Pro", Arial, sans-serif;
  }
  .card {
    position: absolute;
    width: 613px;
    height: 350px;
    background: var(--card);
    box-shadow: 2px 4px 8px rgba(0,0,0,.35);
    overflow: hidden;
  }
  .card--back { left: 96px; top: 110px; }
  .card--front { left: 482px; top: 410px; }

  .side-label {
    position: absolute;
    font-weight: 600;
    font-size: 19px;
    letter-spacing: .5px;
    color: var(--label);
  }
  .side-label--back { left: 116px; top: 472px; }
  .side-label--front { left: 1008px; top: 378px; }

  /* back side */
  .back-brand {
    position: absolute;
    left: 60px; top: 110px;
    display: flex; align-items: center; gap: 22px;
  }
  .brand-dot {
    width: 96px; height: 96px; border-radius: 50%;
    background: var(--lavender-soft);
    flex: none;
  }
  .back-name {
    font-size: 78px; font-weight: 400; color: var(--ink);
    line-height: 1; white-space: nowrap;
  }
  .back-tagline {
    position: absolute; right: 38px; top: 208px;
    font-size: 25px; color: var(--ink); white-space: nowrap;
  }

  /* front side */
  .band {
    height: 126px;
    background: var(--lavender);
    display: flex; flex-direction: column; align-items: center;
    padding-top: 24px;
  }
  .band-name {
    display: flex; align-items: center; gap: 14px;
    font-size: 52px; font-weight: 400; color: var(--ink); line-height: 1;
  }
  .band-dot { width: 38px; height: 38px; border-radius: 50%; background: var(--card); }
  .band-tagline {
    margin-top: 10px;
    font-size: 22px; font-weight: 600; color: var(--ink); letter-spacing: .3px;
  }
  .person { text-align: center; margin-top: 40px; }
  .person-name { font-size: 34px; font-weight: 700; color: var(--ink); line-height: 1.05; }
  .person-role { font-size: 23px; font-weight: 700; color: var(--slate); line-height: 1.2; }
  .contact {
    text-align: center; margin-top: 48px;
    font-size: 18px; font-weight: 600; color: var(--violet-text); line-height: 1.45;
  }
</style>
</head>
<body>
  <section class="card card--back" aria-label="Card back">
    <div class="back-brand">
      <span class="brand-dot"></span>
      <span class="back-name">Lune's Salon</span>
    </div>
    <p class="back-tagline">soft curls bright days</p>
  </section>
  <span class="side-label side-label--back">BACK</span>

  <span class="side-label side-label--front">FRONT</span>
  <section class="card card--front" aria-label="Card front">
    <header class="band">
      <div class="band-name"><span>Lune's</span><span class="band-dot"></span><span>Salon</span></div>
      <p class="band-tagline">soft curls bright days</p>
    </header>
    <div class="person">
      <p class="person-name">LUNE OKAFOR</p>
      <p class="person-role">OWNER / HAIRSTYLIST</p>
    </div>
    <address class="contact" style="font-style:normal">
      (555) 418-6037 | www.lunehairstudio.example<br>
      48390 Harlow Penn Circle | Fairfax, VA 20517
    </address>
  </section>
</body>
</html>
```